NOTE: I PROVIDED THE INCORRECT LOGO AND ONLY A HANDFUL OF PEOPLE NOTICED THAT IT WAS NOT THE ONE I DESCRIBED. THE LOGO I HAVE NOW ATTACHED MATCHES MY WEBSITE AND THE COLORS ON THE WEBSITE SHOULD BE USED FOR THE CARD.

PLEASE READ THE BUSINESS CARD DETAILS AND PROJECT MUST HAVES CAREFULLY.

I am looking for a business card that is powerful, a bit edgy, and although I work in the corporate world, not too formal. I would like to see designs that use the colors on my website www.brightmoorlane.com. I don't want the card to look washed out so please use shades of those colors that make them "pop". The "vibe" of the card needs to show substance and confidence while also reflecting that we're not your usual consultants.

The focus of my work is turning "people problems" into profits. Those problems could be poor service, an unstable workforce, untrained leaders, or managing change. We are an aggressive, results-focused team of performance improvement professionals who refuse to believe "things can't be done". For us, failure is not an option. Our logo reflects a target from the view of the site on a gun.

In addition to the contact information provided on the sample business card (do not include "turning people problems into profits"), I would like to include this statement (probably on the back):
I equip results-oriented business leaders to turn their people problems into profits in six months or less.

PLEASE NOTE THAT MY WEBSITE IS UNDER REVISION TO TONE DOWN THE MILITARY THEME, ALTHOUGH THE WARRIOR ENERGY AND FOCUS ON RESULTS REMAINS.

Target Market(s)

My clients are Mid and senior-level managers. I don't target any particular industry.

Industry/Entity Type

Consulting

Contact Information for Business Card

In addition to the contact information provided on the sample business card (DO NOT INCLUDE "turning people problems into profits"), I would like to include this statement (probably on the back):

I don't care whether the card is landscape or portrait view.

Font styles to use
Sans Serif

Requirements
Must have
• 1. be easy to read, no 6-8 point fonts!
• 2. a "vibe" that captures the eye without being too chaotic or busy
• 3. bold color, not washed out or boring - a good blend with the colors currently on my website (black, red, white, army green) but you don't need to use all of them.
• 4. all the contact information I have provided
• 5. a good blend with the colors currently on my website
• 6. Must have this quote on the back of the card: I equip results-oriented business leaders to turn their people problems into profits in six months or less.
Nice to have
• In looking at the sample images I provided for ideas, you can see that I like the way a card carries over from one side to the next.
• It would be great to find some aspect/quality/feature that I haven't seen before
Should not have
• 1. NO use of ALL CAPS
• 2. fonts that I would have to seek out and purchase (you should provide files for font if using something not standard)

```html
<!DOCTYPE html>
<html lang="en">
<head>
<meta charset="utf-8">
<title>Brightmoor Lane Inc – Business Card</title>
<link rel="stylesheet" href="https://fonts.googleapis.com/css2?family=Questrial&display=swap">
<style>
  :root {
    --army-green: #5a6b2c;
    --carbon: #1c1c1c;
    --signal-red: #c8102e;
    --paper: #ffffff;
    --backdrop: #e6e8ea;
    --ink: #1c1c1c;
  }
  * { margin: 0; padding: 0; box-sizing: border-box; }
  html, body { width: 1200px; height: 880px; overflow: hidden; }
  body {
    background: var(--backdrop);
    font-family: "Questrial", "Century Gothic", sans-serif;
    position: relative;
  }
  .card {
    position: absolute;
    width: 620px;
    height: 360px;
    border-radius: 18px;
    overflow: hidden;
    background: var(--paper);
    box-shadow: 0 10px 28px rgba(0,0,0,0.18);
  }
  .card svg { display: block; width: 100%; height: 100%; }
  .card--front { left: 110px; top: 50px; }
  .card--back  { left: 470px; top: 470px; }
  .fill-green { fill: var(--army-green); }
  .fill-carbon { fill: var(--carbon); }
  .fill-red { fill: var(--signal-red); }
  .wordmark { fill: var(--ink); font-size: 38px; letter-spacing: 0.5px; }
  .wordmark--small { font-size: 32px; }
  .mission { fill: var(--paper); font-size: 14.5px; letter-spacing: 0.3px; }
  .holder-name { fill: var(--paper); font-size: 25px; }
  .holder-title { fill: var(--paper); font-size: 14px; letter-spacing: 0.2px; }
  .contact-line { fill: var(--ink); font-size: 14.5px; }
  .icon-ring { fill: none; stroke: var(--signal-red); stroke-width: 1.6; }
  .icon-glyph { fill: none; stroke: var(--signal-red); stroke-width: 1.4; stroke-linecap: round; stroke-linejoin: round; }
  .divider { stroke: var(--signal-red); stroke-width: 1.2; }
</style>
</head>
<body>

  <section class="card card--front" aria-label="Card front">
    <svg viewBox="0 0 620 360" xmlns="http://www.w3.org/2000/svg">
      <path class="fill-green" d="M0,290 H140 C180,290 180,222 225,222 H520 C560,222 580,205 620,205 V360 H0 Z"/>
      <path class="fill-carbon" d="M0,340 H150 C190,340 188,240 232,240 H540 C575,240 592,226 620,226 V360 H0 Z"/>
      <circle class="fill-red" cx="150" cy="130" r="11"/>
      <text class="wordmark" x="172" y="143">Brightmoor Lane Inc</text>
      <text class="mission" x="258" y="276">I equip results-oriented business leaders</text>
      <text class="mission" x="258" y="298">to turn their people problems into profits</text>
      <text class="mission" x="258" y="320">in six months or less.</text>
    </svg>
  </section>

  <section class="card card--back" aria-label="Card back">
    <svg viewBox="0 0 620 360" xmlns="http://www.w3.org/2000/svg">
      <path class="fill-green" d="M0,0 H620 V16 H430 C402,16 392,30 392,50 C392,70 380,84 350,84 H0 Z"/>
      <path class="fill-carbon" d="M620,16 H430 C402,16 392,30 392,50 V58 H620 Z"/>
      <text class="holder-name" x="32" y="60">Dana Whitfield</text>
      <text class="holder-title" x="602" y="43" text-anchor="end">Chief Performance Strategist</text>

      <circle class="fill-red" cx="40" cy="222" r="10"/>
      <text class="wordmark wordmark--small" x="58" y="234">Brightmoor Lane Inc</text>

      <line class="divider" x1="382" y1="140" x2="382" y2="260"/>

      <g class="contact-row">
        <circle class="icon-ring" cx="406" cy="150" r="8"/>
        <path class="icon-glyph" d="M402,146 c0,5 3,8 8,8 l1,-2 -2,-2 -2,1 c-1,-1 -2,-2 -3,-3 l1,-2 -2,-2 z"/>
        <text class="contact-line" x="422" y="155">555-014-2281</text>
      </g>
      <g class="contact-row">
        <circle class="icon-ring" cx="406" cy="178" r="8"/>
        <rect class="icon-glyph" x="403" y="173" width="6" height="10" rx="1"/>
        <text class="contact-line" x="422" y="183">555-017-6403</text>
      </g>
      <g class="contact-row">
        <circle class="icon-ring" cx="406" cy="206" r="8"/>
        <rect class="icon-glyph" x="401.5" y="202.5" width="9" height="7" rx="0.5"/>
        <path class="icon-glyph" d="M401.5,202.5 L406,206.5 L410.5,202.5"/>
        <text class="contact-line" x="422" y="211">danaw@brightmoorlane.com</text>
      </g>
      <g class="contact-row">
        <circle class="icon-ring" cx="406" cy="234" r="8"/>
        <circle class="icon-glyph" cx="406" cy="234" r="4.5"/>
        <path class="icon-glyph" d="M401.5,234 H410.5 M406,229.5 C404,232 404,236 406,238.5 C408,236 408,232 406,229.5"/>
        <text class="contact-line" x="422" y="239">www.brightmoorlane.com</text>
      </g>

      <rect class="fill-green" x="0" y="310" width="620" height="16"/>
      <rect class="fill-carbon" x="0" y="329" width="620" height="31"/>
    </svg>
  </section>

</body>
</html>
```